Newsletter Design Project

We need a template design for Mailchimp (html) newsletter (two types, one with only one property and one with several). One will be a b2b newsletter the other one a b2c.

It needs to work as a template in mailchimp and be branded like our website www.brightlane-casas-tovira.com

Reason: have not yet found the design that will be the one.

Target Market(s)

b2b: real estate agencies, b2c: real estate buyers in Spain in the middle and luxury segment: €350 k plus

Industry/Entity Type

Property

Requirements
Must have
• mailchimp compatible

```html
<!DOCTYPE html>
<html lang="en">
<head>
<meta charset="utf-8">
<title>Brightlane Casas Tovira – September Property News</title>
<link href="https://fonts.googleapis.com/css2?family=Arimo:wght@400;700&family=Questrial&display=swap" rel="stylesheet">
<style>
  :root {
    --page-bg: #e4e4e4;
    --bar-bg: #3d3d3d;
    --bar-text: #ffffff;
    --tweet: #2fb6e8;
    --like: #6e87c0;
    --forward: #3f9a2a;
    --panel: #ffffff;
    --gold: #d6ca82;
    --gold-text: #d9c97a;
    --ink: #2b2b2b;
    --ink-soft: #444444;
    --rule: #dcdcdc;
    --dark-box: #333333;
  }
  * { box-sizing: border-box; margin: 0; padding: 0; }
  html, body { width: 820px; height: 1200px; overflow: hidden; }
  body { background: var(--page-bg); font-family: "Arimo", Arial, sans-serif; color: var(--ink); position: relative; }

  .top-bar { height: 27px; background: var(--bar-bg); display: flex; align-items: center; justify-content: space-between; padding: 0 8px; }
  .top-links { display: flex; font-size: 12px; }
  .top-links a { color: var(--bar-text); text-decoration: underline; padding: 0 8px; border-left: 1px solid #777; }
  .top-links a:first-child { padding-left: 0; border-left: 0; }
  .share { display: flex; gap: 5px; }
  .share-btn { height: 21px; padding: 0 7px; display: flex; align-items: center; gap: 5px; font-size: 11px; font-weight: 700; color: #fff; border-radius: 2px; }
  .share-btn i { width: 8px; height: 8px; background: #fff; display: block; }
  .share-btn.tweet { background: var(--tweet); }
  .share-btn.like { background: var(--like); }
  .share-btn.forward { background: var(--forward); }

  .sheet { position: absolute; left: 106px; top: 0; width: 608px; }

  .masthead { position: absolute; top: 40px; width: 608px; height: 95px; background: linear-gradient(#ececec, #ffffff); border-bottom: 1px solid #444; }
  .brand { position: absolute; left: 18px; top: 10px; display: flex; align-items: center; gap: 8px; font-family: "Questrial", sans-serif; font-size: 22px; color: #333; letter-spacing: 1px; }
  .brand .mark { width: 14px; height: 14px; background: #333; }
  .brand small { display: block; font-size: 12px; letter-spacing: 2px; }
  .tagline { position: absolute; right: 28px; top: 30px; text-align: right; font-family: "Questrial", sans-serif; font-size: 14.5px; line-height: 20px; color: #444; }

  .issue-title { position: absolute; top: 135px; width: 608px; height: 36px; background: var(--panel); padding: 8px 18px; font-size: 16px; font-weight: 700; color: #444; }

  .feature { position: absolute; top: 177px; width: 608px; height: 357px; background: var(--panel); display: flex; }
  .feature-panel { flex: 0 0 340px; width: 340px; height: 100%; background: var(--gold); position: relative; }
  .feature-box { position: absolute; left: 8px; top: 31px; width: 324px; height: 251px; background: var(--dark-box); }
  .feature-box h2 { height: 40px; line-height: 40px; padding-left: 52px; font-size: 16px; font-weight: 700; color: var(--gold-text); }
  .feature-photo { position: absolute; left: 1px; top: 40px; width: 322px; height: 210px; background: linear-gradient(#7fb0e0 0%, #c95a50 35%, #6e8a4a 60%, #3fa5d6 80%, #d8d8d0 100%); }
  .feature-name { position: absolute; left: 11px; top: 291px; font-size: 15px; letter-spacing: -0.3px; white-space: nowrap; font-weight: 700; color: #333; }
  .feature-text { flex: 1 1 auto; padding: 33px 30px 0 12px; font-size: 12px; line-height: 18px; color: var(--ink-soft); }
  .feature-text .lead { font-weight: 700; color: var(--ink); margin-bottom: 6px; }
  .feature-text p + p { margin-top: 8px; }

  .cta { position: absolute; width: 120px; height: 25px; border-radius: 3px; background: linear-gradient(100deg, #555 0%, #3a3a3a 55%, #111 56%, #222 100%); color: var(--gold-text); font-size: 11px; font-weight: 700; line-height: 25px; text-align: center; }
  .feature-panel .cta { left: 212px; top: 315px; }

  .listings { position: absolute; top: 546px; width: 608px; background: var(--panel); }
  .listing { position: relative; height: 187px; border-bottom: 1px solid var(--rule); }
  .listing:last-child { border-bottom: 0; height: 198px; }
  .listing-photo { position: absolute; left: 10px; top: 11px; width: 250px; height: 168px; border: 2px solid #111; background: linear-gradient(#7fb4e6 0%, #b98a56 40%, #4f8a3e 62%, #2f9fd4 85%, #e0c8a0 100%); }
  .listing-info { position: absolute; left: 278px; top: 14px; width: 300px; font-size: 12px; line-height: 18px; color: var(--ink-soft); }
  .listing-info h3 { font-size: 12px; font-weight: 700; color: var(--ink); margin-bottom: 9px; }
  .listing-info .price { font-weight: 700; color: var(--ink); margin: 7px 0 0 3px; }
  .listing .cta { left: 278px; top: 155px; }

  .footer-nav { position: absolute; top: 1130px; left: 0; width: 820px; text-align: center; font-size: 11px; font-weight: 700; color: #333; }
  .footer-nav span { padding: 0 12px; }
  .copyright { position: absolute; top: 1157px; left: 0; width: 820px; text-align: center; font-size: 11px; color: #333; }
</style>
</head>
<body>
  <header class="top-bar">
    <nav class="top-links">
      <a>Web version</a><a>Edit your subscription</a><a>Unsubscribe</a>
    </nav>
    <div class="share">
      <span class="share-btn tweet"><i></i>TWEET</span>
      <span class="share-btn like"><i></i>LIKE</span>
      <span class="share-btn forward"><i></i>FORWARD</span>
    </div>
  </header>

  <main class="sheet">
    <div class="masthead">
      <div class="brand"><span class="mark"></span><div>BRIGHTLANE<small>CASAS TOVIRA</small></div></div>
      <div class="tagline">Villa Tovira - Property in Vistaluz,<br>Monteclaro, Playasol</div>
    </div>

    <div class="issue-title">September Property News</div>

    <section class="feature">
      <div class="feature-panel">
        <div class="feature-box">
          <h2>Property of the month</h2>
          <div class="feature-photo" role="img" aria-label="Photo of a red villa with white balconies and a curved swimming pool"></div>
        </div>
        <div class="feature-name">Villa for sale in Los Almendros - 499,000 €</div>
        <a class="cta">&lt;&lt; View on website</a>
      </div>
      <div class="feature-text">
        <p class="lead">Lorem Ipsum is simply dummy text of the printing and typesetting industry. Lorem Ipsum has been the industry's standard dummy text ever since the 1500s, when an unknown printer took a galley of type and scrambled it to make a type specimen book.</p>
        <p>It has survived not only five centuries, but also the leap into electronic typesetting, remaining essentially unchanged.</p>
        <p>It has survived not only five centuries, but also the leap into electronic typesetting, remaining essentially unchanged.</p>
      </div>
    </section>

    <section class="listings">
      <article class="listing">
        <div class="listing-photo" role="img" aria-label="Photo of a villa terrace with green awnings, palms and a pool"></div>
        <div class="listing-info">
          <h3>Villa for sale in Los Almendros</h3>
          <p>It has survived not only five centuries, but also the leap into electronic typesetting, remaining essentially unchanged.</p>
          <p class="price">499,000 €</p>
        </div>
        <a class="cta">&lt;&lt; View on website</a>
      </article>
      <article class="listing">
        <div class="listing-photo" role="img" aria-label="Photo of a villa terrace with green awnings, palms and a pool"></div>
        <div class="listing-info">
          <h3>Villa for sale in Los Almendros</h3>
          <p>It has survived not only five centuries, but also the leap into electronic typesetting, remaining essentially unchanged.</p>
          <p class="price">499,000 €</p>
        </div>
        <a class="cta">&lt;&lt; View on website</a>
      </article>
      <article class="listing">
        <div class="listing-photo" role="img" aria-label="Photo of a villa terrace with green awnings, palms and a pool"></div>
        <div class="listing-info">
          <h3>Villa for sale in Los Almendros</h3>
          <p>It has survived not only five centuries, but also the leap into electronic typesetting, remaining essentially unchanged.</p>
          <p class="price">499,000 €</p>
        </div>
        <a class="cta">&lt;&lt; View on website</a>
      </article>
    </section>
  </main>

  <footer>
    <nav class="footer-nav"><span>For Sale</span>|<span>For Rent</span>|<span>Areas</span>|<span>General Info</span>|<span>About us</span>|<span>Contact</span></nav>
    <p class="copyright">Copyright 2010 Brightlane Casas Tovira</p>
  </footer>
</body>
</html>
```